Fire Hydrant Repair Parts Flyer

We need a flyer advertising both fire hydrant parts and the manufacturers that we are stocking. Our company is Coastal Flowline Supply and we are a parts distributor who sells directly to contractors. I have attached an example flyer that advertises some other parts we stock. We don't want it to look exactly like the old flyer, but we would like it to be structured similarly. I have also attached a background image for the flyer as well as some pictures of the parts we are stocking. I have also attached pictures of the manufacturer logos that we are stocking. We are trying to convey the parts that we are stocking which are: "Traffic Repair Kits", "Main Valve Repair Kits", "Extension Kits", "Replacement Caps & Gaskets", "Replacement Nozzles", Adjustable Hydrant Wrenches", "Hydrant Diffusers", & "Hydrant Oil". I have attached pictures of some of these items that we would like placed on the flyer. Let me know if you have any questions at all.

```html
<!DOCTYPE html>
<html lang="en">
<head>
<meta charset="utf-8">
<title>Coastal Flowline Supply – Fire Pump Repair Parts Flyer</title>
<link href="https://fonts.googleapis.com/css2?family=Montserrat:wght@500;700;800;900&display=swap" rel="stylesheet">
<style>
  :root {
    --stage: #2b2b2b;
    --paper: #ffffff;
    --red: #e8184f;
    --hydrant-red: #e4262f;
    --hydrant-dark: #b5131c;
    --blue: #3a4db0;
    --blue-light: #6580c8;
    --splash: #cfe2f4;
    --ink: #121212;
    --brand-blue: #3a4ca8;
  }
  * { margin: 0; padding: 0; box-sizing: border-box; }
  html, body { width: 700px; height: 1200px; overflow: hidden; background: var(--stage); }
  body { font-family: "Montserrat", Arial, sans-serif; }

  .flyer {
    position: absolute; left: 0; top: 105px;
    width: 700px; height: 990px;
    background: var(--paper); overflow: hidden;
  }
  .flyer-bands { position: absolute; inset: 0; }

  .brand {
    position: absolute; left: 44px; top: 28px;
    display: flex; align-items: center; gap: 10px;
  }
  .brand-mark { width: 22px; height: 22px; background: var(--red); }
  .brand-name { font-weight: 500; font-size: 24px; color: var(--brand-blue); letter-spacing: -0.2px; }

  .headline {
    position: absolute; left: 42px; top: 94px;
    font-weight: 900; font-size: 66px; line-height: 61px;
    color: var(--red); letter-spacing: -1px;
  }
  .subhead {
    position: absolute; left: 45px; top: 278px;
    font-weight: 800; font-size: 35px; line-height: 38px;
    color: var(--ink);
  }

  .hero-splash {
    position: absolute; left: 380px; top: 60px; width: 320px; height: 360px;
    border-radius: 50%;
    background: radial-gradient(ellipse at 60% 45%, var(--splash) 0%, rgba(207,226,244,0.5) 45%, rgba(255,255,255,0) 70%);
  }
  .hero-photo {
    position: absolute; left: 448px; top: 52px; width: 200px; height: 492px;
    border-radius: 46px 46px 20px 20px;
    background: linear-gradient(90deg, var(--hydrant-dark) 0%, var(--hydrant-red) 30%, #f04a52 55%, var(--hydrant-red) 75%, var(--hydrant-dark) 100%);
    box-shadow: 0 10px 18px rgba(0,0,0,0.18);
  }

  .part-list { list-style: none; }
  .part-list li {
    position: absolute;
    font-weight: 700; font-size: 18px; line-height: 19px;
    color: var(--paper); text-transform: uppercase;
  }
  .part-list li::before {
    content: ""; position: absolute; left: -22px; top: 4px;
    width: 11px; height: 11px; border-radius: 50%;
    background: var(--paper); border: 3px solid var(--red);
  }

  .maker-badge {
    position: absolute; width: 102px; height: 44px;
    background: var(--paper); border-radius: 6px;
    display: flex; align-items: center; justify-content: center; gap: 6px;
  }
  .maker-dot { width: 12px; height: 12px; border-radius: 50%; background: var(--red); }
  .maker-name { font-weight: 800; font-size: 12px; color: var(--brand-blue); text-transform: uppercase; }

  .product-photo {
    position: absolute; width: 78px; height: 78px; border-radius: 50%;
    border: 6px solid var(--paper);
  }
  .photo-wrench { background: radial-gradient(circle, #b9bec6 0%, #e4e6ea 60%, #f6f7f8 100%); }
  .photo-traffic-kit { background: radial-gradient(circle, #4a4d52 0%, #9ea2a8 55%, #eceef0 100%); }
  .photo-cap { background: radial-gradient(circle, #d3262f 0%, #e98a8f 50%, #f3f3f4 100%); }
  .photo-diffuser { background: radial-gradient(circle, #f2a81c 0%, #f6cf7c 50%, #f6f6f4 100%); }
  .photo-oil { background: radial-gradient(circle, #e2e3e6 0%, #c4c7cc 45%, #f7f7f8 100%); }
  .photo-extension { background: radial-gradient(circle, #2f3135 0%, #8b8f95 55%, #eeeff1 100%); }

  .contact { position: absolute; color: var(--ink); }
  .contact-icon { position: absolute; width: 20px; height: 20px; }
  .phone-number {
    position: absolute; left: 67px; top: 907px;
    font-weight: 800; font-size: 31px; color: var(--red); letter-spacing: -0.3px;
  }
  .web-address { left: 74px; top: 953px; font-weight: 500; font-size: 19px; }
  .email-address { left: 396px; top: 914px; font-weight: 500; font-size: 14.5px; }
  .street-address { left: 402px; top: 945px; font-weight: 500; font-size: 14.5px; line-height: 17px; }
</style>
</head>
<body>
<main class="flyer">
  <svg class="flyer-bands" width="700" height="990" viewBox="0 0 700 990" aria-hidden="true">
    <path d="M0,352 C180,400 430,450 700,372 L700,990 L0,990 Z" fill="var(--blue-light)"/>
    <path d="M0,420 C200,470 440,480 700,430 L700,990 L0,990 Z" fill="var(--blue)"/>
    <path d="M0,893 C250,900 500,862 700,800 L700,990 L0,990 Z" fill="var(--red)"/>
    <path d="M0,893 C250,902 500,882 700,838 L700,990 L0,990 Z" fill="var(--paper)"/>
    <g stroke="#ffffff" stroke-opacity="0.8" stroke-width="1.2">
      <line x1="541" y1="555" x2="541" y2="800"/>
      <line x1="521" y1="616" x2="560" y2="616"/>
      <line x1="521" y1="705" x2="560" y2="705"/>
      <line x1="521" y1="795" x2="560" y2="795"/>
    </g>
  </svg>

  <div class="brand">
    <span class="brand-mark" aria-hidden="true"></span>
    <span class="brand-name">Coastal Flowline Supply</span>
  </div>

  <div class="hero-splash" aria-hidden="true"></div>
  <div class="hero-photo" role="img" aria-label="Photo of a red fire hydrant with chains and a splash of water"></div>

  <h1 class="headline">FIRE<br>PUMP<br>REPAIR</h1>
  <h2 class="subhead">PARTS AND<br>ACCESSORIES</h2>

  <ul class="part-list">
    <li style="left:79px; top:523px;">Traffic<br>Repair Kits</li>
    <li style="left:79px; top:573px;">Main Valve<br>Repair Kits</li>
    <li style="left:79px; top:620px;">Extension<br>Kits</li>
    <li style="left:79px; top:670px;">Hydrant<br>Diffusers</li>
    <li style="left:234px; top:523px;">Replacement<br>Caps &amp; Gaskets</li>
    <li style="left:234px; top:573px;">Replacement<br>Nozzles</li>
    <li style="left:234px; top:620px;">Adjustable<br>Hydrant<br>Wrenches</li>
    <li style="left:234px; top:689px;">Hydrant Oil</li>
  </ul>

  <div class="maker-badge" style="left:46px; top:741px;"><span class="maker-dot"></span><span class="maker-name">Harborline</span></div>
  <div class="maker-badge" style="left:165px; top:741px;"><span class="maker-dot"></span><span class="maker-name">Ridgeway</span></div>
  <div class="maker-badge" style="left:284px; top:741px;"><span class="maker-dot"></span><span class="maker-name">Tidewater</span></div>
  <div class="maker-badge" style="left:46px; top:798px;"><span class="maker-dot"></span><span class="maker-name">Summit Co.</span></div>
  <div class="maker-badge" style="left:165px; top:798px;"><span class="maker-dot"></span><span class="maker-name">Keelson</span></div>
  <div class="maker-badge" style="left:284px; top:798px;"><span class="maker-dot"></span><span class="maker-name">Northgate</span></div>

  <div class="product-photo photo-wrench" style="left:443px; top:577px;" role="img" aria-label="Adjustable hydrant wrench"></div>
  <div class="product-photo photo-traffic-kit" style="left:561px; top:577px;" role="img" aria-label="Traffic repair kit parts"></div>
  <div class="product-photo photo-cap" style="left:443px; top:666px;" role="img" aria-label="Red replacement cap with chain"></div>
  <div class="product-photo photo-diffuser" style="left:561px; top:666px;" role="img" aria-label="Yellow hydrant diffuser with gauge"></div>
  <div class="product-photo photo-oil" style="left:443px; top:756px;" role="img" aria-label="Bottle of hydrant oil"></div>
  <div class="product-photo photo-extension" style="left:561px; top:756px;" role="img" aria-label="Extension kit components"></div>

  <svg class="contact-icon" style="left:34px; top:918px;" viewBox="0 0 20 20" aria-hidden="true">
    <circle cx="10" cy="10" r="10" fill="var(--blue)"/>
    <path d="M7 5.5c.6-.4 1.2-.2 1.5.4l.7 1.5c.2.5 0 1-.4 1.3l-.5.4c.5 1.1 1.3 1.9 2.4 2.4l.4-.5c.3-.4.8-.6 1.300-.4l1.5.7c.6.3.8.9.4 1.5-.6 1-1.7 1.4-2.8 1-2.6-.9-4.6-2.9-5.5-5.5-.4-1.1 0-2.2 1-2.8z" fill="#fff"/>
  </svg>
  <div class="phone-number">(800) 555-0142</div>

  <svg class="contact-icon" style="left:34px; top:956px;" viewBox="0 0 20 20" aria-hidden="true">
    <circle cx="10" cy="10" r="10" fill="var(--blue)"/>
    <g fill="none" stroke="#fff" stroke-width="1.2">
      <circle cx="10" cy="10" r="5.5"/>
      <ellipse cx="10" cy="10" rx="2.4" ry="5.5"/>
      <line x1="4.5" y1="10" x2="15.5" y2="10"/>
    </g>
  </svg>
  <div class="contact web-address">www.coastalflowline.com</div>

  <svg class="contact-icon" style="left:368px; top:914px;" viewBox="0 0 20 20" aria-hidden="true">
    <circle cx="10" cy="10" r="10" fill="var(--blue)"/>
    <rect x="5" y="6.5" width="10" height="7" rx="1" fill="none" stroke="#fff" stroke-width="1.3"/>
    <path d="M5.5 7.2 L10 10.8 L14.5 7.2" fill="none" stroke="#fff" stroke-width="1.3"/>
  </svg>
  <div class="contact email-address">service@coastalflowline.com</div>

  <svg class="contact-icon" style="left:368px; top:946px;" viewBox="0 0 20 20" aria-hidden="true">
    <circle cx="10" cy="10" r="10" fill="var(--blue)"/>
    <path d="M10 4.5a3.6 3.6 0 0 0-3.6 3.6c0 2.7 3.6 7 3.6 7s3.6-4.3 3.6-7A3.6 3.6 0 0 0 10 4.5z" fill="#fff"/>
    <circle cx="10" cy="8.1" r="1.4" fill="var(--blue)"/>
  </svg>
  <div class="contact street-address">1420 Harbor Point Road<br>Pensacola FL 32502</div>
</main>
</body>
</html>
```